Marlow Pantry Co makers of various food product lines for Australian market

We need a label design concept for various product lines , this concept should have common elements across the lines. The labels within the lines would need to be specific to the individual products. The initial product lines will include the following, Sauces (mild to very hot) , Meat products, dried and fresh (Biltong to Boerewors) and also ready prepared uncooked meat products (marinated chicken portions, chicken wings etc). The target customers will be in two categories. Firstly, individuals (often ex South African residents) looking to purchase the specific sauces and meat products in smaller portion packaging. Second, distribution to select restaurants and pubs , different products to specific business types. ie bulk sauces and prepared products to restaurants and Biltong type products to pubs for snacks etc. The products currently being made are Portuguese style Peri Peri sauce (mild, original) , Peri Peri sauce (hot with Habanero chillies) and Biltong (dried meat snack similar to Jerky). The sauces are being sold to friends and family and word of mouth customers in hand labeled 240 ml bottles , the Biltong is sold via a Facebook group and word of mouth customers with very basic labels onto brown paper packets. We will be marketing the products as current, as well as Farmers markets and direct contact with selected restaurants and pubs. The products are made using traditional recipes and methods. Proposed label size 64mm h x 108 mm w. The theme should have a slightly rustic African feel to it.

```html
<!DOCTYPE html>
<html lang="en">
<head>
<meta charset="utf-8">
<title>Marlow Pantry Co – Product Label</title>
<link rel="stylesheet" href="https://fonts.googleapis.com/css2?family=Open+Sans:wght@400;600&family=Roboto+Condensed:wght@700&family=Dancing+Script:wght@600&family=Nothing+You+Could+Do&display=swap">
<style>
  :root {
    --page: #f2f2f2;
    --label-red: #c4161c;
    --band-black: #111111;
    --band-smoke: #2a2a2a;
    --frame-green: #7cc21e;
    --frame-black: #1a1a1a;
    --frame-line: #d9d9d9;
    --panel-line: #f3a3a3;
    --ink-white: #ffffff;
    --ink-chalk: #cfcfcf;
    --ink-dark: #120505;
    --font-sans: "Open Sans", Arial, sans-serif;
    --font-small: "Roboto Condensed", "Arial Narrow", sans-serif;
    --font-script: "Dancing Script", cursive;
    --font-chalk: "Nothing You Could Do", cursive;
  }
  html, body {
    margin: 0;
    width: 1200px;
    height: 800px;
    overflow: hidden;
    background: var(--page);
  }
  .label {
    position: absolute;
    left: 60px;
    top: 80px;
    width: 1080px;
    height: 640px;
  }
  .label-frame {
    position: absolute;
    inset: 0;
  }
  .label-text {
    position: absolute;
    margin: 0;
  }
  .heading {
    font-family: var(--font-sans);
    font-weight: 600;
    font-size: 23px;
    color: var(--ink-white);
  }
  .fine-print {
    font-family: var(--font-small);
    font-weight: 700;
    font-size: 12.5px;
    line-height: 22px;
    letter-spacing: -0.2px;
  }
  .fine-print--light { color: var(--ink-white); }
  .fine-print--dark { color: var(--ink-dark); }
  .chalk {
    font-family: var(--font-chalk);
    font-size: 30px;
    color: var(--ink-chalk);
  }
  .script-tag {
    font-family: var(--font-script);
    font-size: 38px;
    color: var(--ink-white);
  }
  .badge-kicker {
    font-family: var(--font-sans);
    font-size: 22px;
    color: var(--ink-white);
    width: 1080px;
    left: 0;
    text-align: center;
  }
  .brand-name {
    font-family: var(--font-sans);
    font-weight: 400;
    font-size: 33px;
    color: var(--label-red);
    width: 1080px;
    left: 0;
    text-align: center;
    letter-spacing: 1px;
  }
</style>
</head>
<body>
  <div class="label">
    <svg class="label-frame" width="1080" height="640" viewBox="0 0 1080 640" aria-hidden="true">
      <defs>
        <linearGradient id="band-smoke" x1="0" y1="0" x2="1" y2="1">
          <stop offset="0" stop-color="var(--band-smoke)"/>
          <stop offset="0.5" stop-color="var(--band-black)"/>
          <stop offset="1" stop-color="var(--band-smoke)"/>
        </linearGradient>
        <linearGradient id="badge-fill" x1="0" y1="0" x2="0" y2="1">
          <stop offset="0" stop-color="#1c1c1c"/>
          <stop offset="1" stop-color="#000000"/>
        </linearGradient>
      </defs>
      <!-- outer frame: black base with green sweep on the left -->
      <rect x="0" y="0" width="1080" height="640" fill="var(--frame-black)"/>
      <polygon points="0,0 418,0 623,640 0,640" fill="var(--frame-green)"/>
      <rect x="12" y="12" width="1056" height="616" fill="none" stroke="var(--frame-line)" stroke-width="3"/>
      <!-- red panel -->
      <rect x="27" y="27" width="1022" height="582" fill="var(--label-red)"/>
      <rect x="31" y="31" width="1014" height="574" fill="none" stroke="var(--panel-line)" stroke-width="2"/>
      <!-- black middle band -->
      <rect x="31" y="171" width="1014" height="232" fill="url(#band-smoke)"/>
      <!-- hexagon badge -->
      <polygon points="315,295 425,103 650,103 760,295 650,487 425,487" fill="url(#badge-fill)" stroke="var(--ink-white)" stroke-width="3"/>
      <polygon points="324,295 430,111 645,111 751,295 645,479 430,479" fill="none" stroke="#555" stroke-width="1"/>
      <!-- plain circle beside the name -->
      <circle cx="537" cy="408" r="58" fill="var(--label-red)"/>
    </svg>

    <!-- top strip -->
    <p class="label-text heading" style="left:40px; top:40px;">Lorem ipsum dolor.</p>
    <p class="label-text fine-print fine-print--light" style="left:40px; top:76px;">Lorem ipsum dolor sit<br>amet, consectLorem ipsum<br>dolor sit amet, consec</p>
    <p class="label-text heading" style="left:790px; top:40px;">Lorem ipsum dolor.</p>
    <p class="label-text fine-print fine-print--light" style="left:790px; top:76px;">Lorem ipsum dolor sit<br>amet, consectLorem ipsum<br>dolor sit amet, consec</p>

    <!-- black band -->
    <p class="label-text chalk" style="left:70px; top:180px;">Lorem ipsum</p>
    <p class="label-text fine-print fine-print--light" style="left:70px; top:232px;">Lorem ipsum dolor sit<br>amet, consectLorem ipsum<br>dolor sit amet, consec</p>
    <p class="label-text chalk" style="left:70px; top:320px;">Lorem ipsum</p>
    <p class="label-text chalk" style="left:785px; top:180px;">Lorem ipsum</p>
    <p class="label-text fine-print fine-print--light" style="left:785px; top:232px;">Lorem ipsum dolor sit<br>amet, consectLorem ipsum<br>dolor sit amet, consec</p>
    <p class="label-text chalk" style="left:785px; top:320px;">Lorem ipsum</p>

    <!-- badge content -->
    <p class="label-text badge-kicker" style="top:118px;">Lorem ipsum</p>
    <p class="label-text brand-name" style="top:220px;">Marlow Pantry Co</p>

    <!-- bottom strip -->
    <p class="label-text fine-print fine-print--dark" style="left:60px; top:418px;">Lorem ipsum dolor sit amet,<br>consectetuer adipiscing elit,<br>sed diam nonummy nibh<br>euismod tincidunt ut laoreet<br>dolore magna aliquam erat<br>volutpat. Ut wisi enim ad<br>minim veniam, quis nostrud</p>
    <p class="label-text fine-print fine-print--dark" style="left:790px; top:418px;">Lorem ipsum dolor sit amet,<br>consectetuer adipiscing elit,<br>sed diam nonummy nibh<br>euismod tincidunt ut laoreet<br>dolore magna aliquam erat<br>volutpat. Ut wisi enim ad<br>minim veniam, quis nostrud</p>
    <p class="label-text script-tag" style="left:440px; top:520px;">Lorem ipsum</p>
  </div>
</body>
</html>
```